Starting number decals Motorsport
Frost Rally Days 2013
Now it is only 1 day and 14 hours left!!!
torvald
We have some excellent suggestions and to see how the sticker will look on a car in the real world,
we have loaded a picture now We send a test picture that it is possible to test mount the decal on the side of the car, we want to mount on the front door of the car, the picture is uploaded now
We want to try to tilt the stratnumer figures a little forward as PRIMTOUR
We have now updated with sponsor logo will be featured on the decal
KR/WTF/HV Team.
Forgot to inform that 5 year anniversary is this year and it should be, if possible, preferably also in 2013

```html
<!DOCTYPE html>
<html lang="sv">
<head>
<meta charset="utf-8">
<title>Frost Rally Days 2013 – Starting number decal</title>
<link href="https://fonts.googleapis.com/css2?family=Russo+One&family=Roboto+Condensed:wght@700;900&display=swap" rel="stylesheet">
<style>
  :root{
    --red:#d3202c;
    --red-dark:#7d1118;
    --black:#111;
    --white:#fff;
    --flag-blue:#1f4f9c;
    --flag-yellow:#f6c400;
  }
  html,body{margin:0;padding:0;overflow:hidden;background:var(--white);}
  .decal-sheet{position:relative;width:1200px;height:712px;overflow:hidden;background:var(--white);font-family:"Roboto Condensed",Arial,sans-serif;}

  .hatch-band{position:absolute;height:12px;
    background:repeating-linear-gradient(115deg,var(--red) 0 7px,transparent 7px 11px);}
  .hatch-band--top{left:340px;width:505px;top:22px;}

  .event-name{position:absolute;left:340px;top:70px;width:256px;text-align:center;white-space:nowrap;
    color:var(--red);font-family:"Russo One",sans-serif;font-size:24px;line-height:1.2;}
  .event-sub{position:absolute;left:340px;top:110px;width:256px;text-align:center;white-space:nowrap;
    color:var(--black);font-weight:700;font-size:13px;line-height:1.2;}
  .divider{position:absolute;left:604px;top:62px;width:2px;height:72px;background:var(--black);}
  .sponsor-area{position:absolute;left:628px;top:94px;font-weight:900;font-size:24px;
    letter-spacing:1px;color:var(--black);white-space:nowrap;}

  .start-number{position:absolute;left:0;width:1200px;text-align:center;margin:0;white-space:nowrap;
    font-family:"Russo One",sans-serif;color:var(--red);}
  .start-number--main{top:148px;font-size:150px;line-height:1;letter-spacing:10px;
    transform:skewX(-8deg);text-shadow:5px 5px 0 var(--red-dark);}
  .class-code{position:absolute;left:0;width:1200px;top:296px;text-align:center;
    font-family:"Russo One",sans-serif;font-size:66px;line-height:1;color:var(--black);}

  .info-band{position:absolute;left:343px;top:391px;width:502px;height:40px;background:var(--red);}
  .info-band span{position:absolute;top:9px;color:var(--white);font-weight:900;font-size:20px;letter-spacing:1px;}
  .info-band .inspection{left:20px;}
  .info-band .speed-time{right:24px;}
  .flag-badge{position:absolute;left:512px;top:380px;}

  .site-row{position:absolute;left:343px;top:500px;width:502px;height:30px;}
  .site-row .hatch-band{top:8px;height:12px;}
  .site-row .hatch-band--left{left:0;width:135px;}
  .site-row .hatch-band--right{right:0;width:135px;}
  .site-row .rule{position:absolute;left:0;right:0;top:26px;height:3px;background:var(--red);}
  .site-name{position:absolute;left:0;right:0;top:0;text-align:center;color:var(--red);
    font-weight:900;font-size:26px;line-height:28px;letter-spacing:1px;}

  .digit-set{top:548px;font-size:160px;line-height:1;letter-spacing:8px;
    transform:skewX(-8deg);text-shadow:5px 5px 0 var(--red-dark);}
</style>
</head>
<body>
<main class="decal-sheet">
  <div class="hatch-band hatch-band--top"></div>

  <div class="event-name">Frost Rally Days</div>
  <div class="event-sub">5th Anniversary VARBY 15-16/2 2013</div>
  <div class="divider"></div>
  <div class="sponsor-area">SPONSOR AREA</div>

  <p class="start-number start-number--main">1234</p>
  <div class="class-code">16 BD</div>

  <div class="info-band">
    <span class="inspection">BESIKTNING</span>
    <span class="speed-time">FART / TID</span>
  </div>
  <svg class="flag-badge" width="176" height="104" viewBox="0 0 176 104" aria-label="Swedish flag">
    <defs>
      <clipPath id="flag-shape"><polygon points="8,4 168,4 128,98 48,98"/></clipPath>
    </defs>
    <polygon points="0,0 176,0 132,104 44,104" fill="var(--white)"/>
    <g clip-path="url(#flag-shape)">
      <rect x="0" y="0" width="176" height="104" fill="var(--flag-blue)"/>
      <rect x="0" y="42" width="176" height="18" fill="var(--flag-yellow)"/>
      <rect x="64" y="0" width="20" height="104" fill="var(--flag-yellow)"/>
    </g>
  </svg>

  <div class="site-row">
    <div class="hatch-band hatch-band--left"></div>
    <div class="hatch-band hatch-band--right"></div>
    <div class="site-name">TRACKRUSH.SE</div>
    <div class="rule"></div>
  </div>

  <p class="start-number digit-set">1234567890</p>
</main>
</body>
</html>
```